New audiology website PSD design only - guaranteed

We need a clean and attractive website to replace an existing Audiology (hearing technology) website which will be wordpress based.
The current website is: http://pelmorahearing.com.au
They have a new logo and colors which you can find at www.quodel.net/temp/plh2018.pdf
We will no longer have a web shop in the new website
To enter the competition, we only need a sample of the home page.
The winning design will be asked to produce 2 standard page template alternatives as well (based on the winning home page design, but for a standard page layout)
The winning design must provide any photos used
We want a clean, credible site but with some warmth
Target Market(s)
All ages but needs to include the elderly
Industry/Entity Type
Medical And Science
Number of Pages Required
3 page
Look and feel
Each slider illustrates characteristics of the customer's brand and the style your logo design should communicate.

```html
<!DOCTYPE html>
<html lang="en">
<head>
<meta charset="utf-8">
<title>PelmoraHearing – Home</title>
<link rel="stylesheet" href="https://fonts.googleapis.com/css2?family=Oswald:wght@400;500;600&family=Poppins:ital,wght@0,400;0,500;0,600;0,700;1,400;1,500&display=swap">
<style>
:root{
  --orange:#f47a2d;
  --dark:#3c3c3c;
  --text:#6f6f6f;
  --light:#f4f4f4;
  --footer:#1c1c1c;
  --white:#ffffff;
  --tile-orange:#f37021;
  --tile-blue:#3fb1f3;
  --tile-green:#45c95c;
  --tile-teal:#5fcfca;
  --tile-coral:#ef6a5a;
  --tile-purple:#a36fd6;
}
*{margin:0;padding:0;box-sizing:border-box}
html,body{width:699px;height:1200px;overflow:hidden}
body{font-family:'Poppins',sans-serif;color:var(--text);background:var(--white);position:relative}
section,header,footer{position:absolute;left:0;width:699px}
.abs{position:absolute}

/* hero */
.hero{top:0;height:349px;overflow:hidden}
.hero-photo{position:absolute;inset:0;background:linear-gradient(90deg,#d9d2a8 0%,#e2dcb9 35%,#cdbf9c 60%,#b89a7c 80%,#e9e4d8 100%)}
.hero-fade{position:absolute;left:0;right:0;bottom:0;height:90px;background:linear-gradient(180deg,rgba(255,255,255,0),rgba(240,236,226,.6))}
.brand{left:80px;top:26px;display:flex;align-items:center;gap:4px;font-weight:600;font-size:15px;color:var(--orange)}
.brand-dot{width:14px;height:14px;border-radius:50%;border:2px solid var(--orange)}
.call-btn{left:529px;top:11px;width:91px;height:16px;border-radius:8px;background:var(--dark);color:var(--white);font-size:6px;font-weight:700;text-align:center;line-height:16px}
.main-nav{left:279px;top:34px;display:flex;gap:12px;font-size:6.2px;font-weight:700;color:#333;text-transform:uppercase}
.main-nav .current{color:var(--orange);border-bottom:1px solid var(--orange);padding-bottom:3px}
.slide-arrow{left:48px;top:139px}
.hero-title{left:84px;top:135px;font-family:'Oswald',sans-serif;font-weight:500;font-size:19.5px;color:#3a3a3a;letter-spacing:.3px}
.hero-title span{color:var(--orange)}
.hero-sub{left:84px;top:165px;font-family:'Oswald',sans-serif;font-style:italic;font-weight:400;font-size:9px;color:var(--orange)}
.hero-copy{left:84px;top:184px;width:225px;font-size:6px;font-style:italic;line-height:10.5px;color:#444}
.btn{display:block;text-align:center;font-size:5.6px;font-weight:600;font-style:italic;color:var(--white);border-radius:9px}
.btn-dark{left:84px;top:229px;width:71px;height:17px;line-height:17px;background:#474747}
.btn-orange{left:161px;top:229px;width:83px;height:17px;line-height:17px;background:var(--orange)}
.slide-dots{left:92px;top:262px;display:flex;gap:8px}
.slide-dots i{width:4px;height:4px;border-radius:50%;background:#555}
.slide-dots i.on{background:var(--orange)}

/* services */
.services{top:349px;height:181px;background:var(--white)}
.tile{width:80px;height:57px;color:var(--white);font-size:4.8px;font-weight:700;text-transform:uppercase;text-align:center;display:flex;flex-direction:column;align-items:center;justify-content:flex-end;padding-bottom:6px;gap:5px}
.tile svg{width:20px;height:20px}
.t1{left:77px;top:24px;background:var(--tile-orange)}
.t2{left:177px;top:24px;background:var(--tile-blue)}
.t3{left:278px;top:24px;background:var(--tile-green)}
.t4{left:77px;top:94px;background:var(--tile-teal)}
.t5{left:177px;top:94px;background:var(--tile-coral)}
.t6{left:278px;top:94px;background:var(--tile-purple)}
.section-title{font-size:9px;font-weight:700;color:#333;text-transform:uppercase}
.section-title span{color:var(--orange)}
.services-text{left:377px;top:24px;width:245px}
.services-text .kicker{font-size:5.4px;margin-top:2px}
.services-text p{font-size:6px;line-height:10.6px;margin-top:6px}
.outline-btn{left:379px;top:120px;width:115px;height:20px;border:1px solid #ccc;border-radius:10px;font-size:5px;font-weight:700;color:#333;display:flex;align-items:center;justify-content:center;gap:8px}

/* modern audiology */
.modern{top:530px;height:211px;background:var(--light);border-top:1px solid #e6e6e6}
.modern-photo{left:409px;top:0;width:290px;height:211px;background:linear-gradient(90deg,rgba(244,244,244,1) 0%,#e7e2e4 30%,#d9d6dc 55%,#cfc7c2 75%,#e8e4e2 100%)}
.modern-text{left:81px;top:27px;width:340px}
.modern-text .kicker{font-size:5.6px;font-weight:600;color:#444;margin-top:2px}
.modern-text p{font-size:6.1px;line-height:12.4px;margin-top:5px}

/* doctors */
.doctors{top:741px;height:234px;background:var(--white)}
.doctors-photo{left:0;top:0;width:327px;height:234px;background:linear-gradient(120deg,#c9b4a0 0%,#e6e8ee 45%,#d6e0ec 70%,#8aa6c9 100%)}
.doctors-text{left:339px;top:27px;width:290px}
.doctors-text .kicker{font-size:5.4px;margin-top:2px}
.doctors-text .kicker b{color:var(--orange);font-weight:400}
.doctors-text p{font-size:6px;line-height:10.6px;margin-top:4px}
.doc-card{top:111px;width:58px;text-align:center}
.doc-photo{width:58px;height:50px;border:2px solid #ddd;background:linear-gradient(180deg,#e9eef3,#c7d3df)}
.doc-card h4{font-size:5.2px;font-weight:600;color:#333;margin-top:6px;text-transform:uppercase}
.doc-card small{display:block;font-size:4.2px;color:#444;margin-top:1px}
.carousel-next{left:557px;top:130px;width:11px;height:11px;border:1px solid #bbb;border-radius:50%}
.btn-square{left:346px;top:197px;width:68px;height:17px;line-height:17px;background:var(--orange);color:var(--white);font-size:5.6px;text-align:center}

/* contact band */
.contact-band{top:975px;height:73px;background:var(--orange);color:var(--white)}
.contact-item{top:16px;display:flex;gap:12px}
.contact-item svg{width:28px;height:28px}
.contact-item h5{font-size:6.4px;font-weight:700;text-transform:uppercase;margin-top:2px}
.contact-item p{font-size:6.2px;margin-top:3px}
.contact-item em{display:block;font-size:5.4px}
.ci-call{left:82px}
.ci-mail{left:266px}
.ci-news{left:437px}
.news-field{width:140px;border-bottom:1px solid rgba(255,255,255,.8);font-size:4.6px;font-style:italic;padding:4px 0 3px 2px;display:flex;justify-content:space-between;margin-top:3px}

/* footer */
.site-footer{top:1048px;height:152px;background:var(--footer);color:#cfcfcf}
.foot-head{top:22px;font-size:6.2px;font-weight:700;color:var(--orange);text-transform:uppercase}
.foot-col{top:40px;font-size:5.6px;line-height:12.4px}
.foot-col h6{font-size:6.6px;font-weight:600;color:var(--orange);margin-bottom:1px}
.foot-col em{color:var(--orange)}
.foot-rule{left:0;top:116px;width:699px;height:1px;background:#333}
.copyright{left:82px;top:128px;font-size:4px;color:#888}
.social{left:556px;top:126px;display:flex;gap:10px}
.social i{width:10px;height:10px;border-radius:50%;background:#4a6fa5}
</style>
</head>
<body>

<header class="hero">
  <div class="hero-photo" role="img" aria-label="Photo of a smiling boy having his ear examined by a doctor with an otoscope"></div>
  <div class="hero-fade"></div>
  <div class="abs brand"><span class="brand-dot"></span>PelmoraHearing</div>
  <div class="abs call-btn">CALL : (02) 5550 1842</div>
  <nav class="abs main-nav">
    <span class="current">Home</span><span>Your Hearing</span><span>Musicians</span><span>Doctors Information</span><span>About Us</span><span>Products</span><span>Contact Us</span>
  </nav>
  <svg class="abs slide-arrow" width="10" height="16" viewBox="0 0 10 16"><path d="M8 1 2 8l6 7" fill="none" stroke="#9a9580" stroke-width="1.5"/></svg>
  <h1 class="abs hero-title">ENJOY THE SOUNDS <span>OF THE LIFE..!</span></h1>
  <div class="abs hero-sub">Find out what better hearing can mean for you.</div>
  <p class="abs hero-copy">Lorem ipsum dolor sit amet, consectetuer adipiscing elit. Aenean commodo ligula eget dolor. Aenean massa. Cum sociis natoque penatibus et magnis dis parturient montes, nascetur ridiculus mus. Donec quam</p>
  <a class="abs btn btn-dark">More Details</a>
  <a class="abs btn btn-orange">Book An Appointment</a>
  <div class="abs slide-dots"><i class="on"></i><i></i><i></i><i></i></div>
</header>

<section class="services">
  <div class="abs tile t1"><svg viewBox="0 0 24 24" fill="none" stroke="#fff" stroke-width="1.6"><path d="M8 20c2 0 3-2 4-4s3-3 3-7a5 5 0 0 0-10 0"/><path d="M16 4a8 8 0 0 1 2 5M19 2a11 11 0 0 1 3 7"/></svg>Pure Tone Audiology</div>
  <div class="abs tile t2"><svg viewBox="0 0 24 24" fill="none" stroke="#fff" stroke-width="1.6"><circle cx="10" cy="10" r="6"/><path d="M8 16v6M17 8v6M20 6v10M23 9v4"/></svg>Speech Testing</div>
  <div class="abs tile t3"><svg viewBox="0 0 24 24" fill="none" stroke="#fff" stroke-width="1.6"><path d="M6 10a6 6 0 0 1 12 0c0 4-4 5-4 9a3 3 0 0 1-5 1"/><circle cx="12" cy="10" r="2"/></svg>Tympanometry</div>
  <div class="abs tile t4"><svg viewBox="0 0 24 24" fill="none" stroke="#fff" stroke-width="1.6"><path d="M4 16v-4a8 8 0 0 1 16 0v4"/><rect x="3" y="14" width="4" height="7" rx="1"/><rect x="17" y="14" width="4" height="7" rx="1"/></svg>Paediatric Hearing Test</div>
  <div class="abs tile t5"><svg viewBox="0 0 24 24" fill="none" stroke="#fff" stroke-width="1.6"><path d="M12 4c-5 0-8 3-8 7 0 3 2 5 5 5h2v5M12 4c5 0 8 3 8 7 0 3-2 5-5 5"/><path d="M12 4v9"/></svg>Auditory Brainstem</div>
  <div class="abs tile t6"><svg viewBox="0 0 24 24" fill="none" stroke="#fff" stroke-width="1.6"><rect x="4" y="6" width="16" height="7" rx="2"/><path d="M7 13v5h10v-5"/></svg>Videonystagmography</div>
  <div class="abs services-text">
    <h2 class="section-title">Our Services</h2>
    <div class="kicker">Our Departments &amp; Special Services</div>
    <p>PelmoraHearing is a leading Hearing and Balance Clinic located in the inner suburbs of Sydney. Each of our custom built clinics have the most up to date diagnostic equipment available. We offer an extensive range of diagnostics conducted by highly experienced and fully trained Audiologists. We work closely with medical professionals to deliver outstanding and reliable services.</p>
  </div>
  <a class="abs outline-btn">ALL DEPARTMENTS &amp; SERVICES <svg width="8" height="6" viewBox="0 0 8 6"><path d="M0 3h7M5 1l2 2-2 2" fill="none" stroke="#f47a2d"/></svg></a>
</section>

<section class="modern">
  <div class="abs modern-photo" role="img" aria-label="Close-up photo of a hand holding a behind-the-ear hearing aid"></div>
  <div class="abs modern-text">
    <h2 class="section-title">We'r the best in <span>Modern Audiology</span></h2>
    <div class="kicker">We Provide Most Professional service since 1950</div>
    <p>PelmoraHearing is an independently owned and managed professional audiology clinic. Our Audiologists are health-care professionals specialising in diagnosing, treating and monitoring everything to do with hearing and balance. At PelmoraHearing we work closely with Ear, Nose and Throat specialists to ensure you receive the highest standards of medical care.</p>
    <p>PelmoraHearing are state of the art hearing and balance clinics. We provide all brands of digital hearing aids, cochlear implants and assisted listening devices. We are diagnostic clinics, offering hearing tests for adults and children, balance tests, tinnitus testing and treatment, and auditory processing tests (APD).</p>
    <p>At PelmoraHearing we are committed to excellence, we are at the forefront of providing detailed testing and treatment options. Our state-of-the-art clinics are purpose built, and our fully accredited Audiology team are experienced and at the top of their profession. Our success is measured by your satisfaction.</p>
  </div>
</section>

<section class="doctors">
  <div class="abs doctors-photo" role="img" aria-label="Photo of a doctor examining a young boy's ear with an otoscope"></div>
  <div class="abs doctors-text">
    <h2 class="section-title"><span>Our</span> Doctors</h2>
    <div class="kicker">For appointments please phone <b>5550 1842</b></div>
    <p>PelmoraHearing is one of Sydney's leading diagnostic hearing and balance clinics. Referring doctors can be assured that all testing and rehabilitation is reviewed to the highest industry standards. Our Audiologists also work closely with referring ENT's and Doctors to ensure all testing meets the needs of their practice.</p>
  </div>
  <div class="abs doc-card" style="left:342px"><div class="doc-photo" role="img" aria-label="Portrait photo of a doctor"></div><h4>Marcus Leland</h4><small>Tympanometry Specilist</small></div>
  <div class="abs doc-card" style="left:418px"><div class="doc-photo" role="img" aria-label="Portrait photo of a doctor"></div><h4>Priya Varden</h4><small>Tympanometry Specilist</small></div>
  <div class="abs doc-card" style="left:490px"><div class="doc-photo" role="img" aria-label="Portrait photo of a doctor"></div><h4>Thomas Quill</h4><small>Tympanometry Specilist</small></div>
  <svg class="abs carousel-next" viewBox="0 0 11 11"><path d="M4.5 3l2 2.5-2 2.5" fill="none" stroke="#999"/></svg>
  <a class="abs btn-square">View all Doctors &nbsp;›</a>
</section>

<section class="contact-band">
  <div class="abs contact-item ci-call">
    <svg viewBox="0 0 28 28" fill="none" stroke="#fff" stroke-width="1.3"><rect x="2" y="6" width="6" height="18" rx="2"/><rect x="8" y="4" width="18" height="20" rx="2"/><path d="M12 10h10M12 14h2M16 14h2M20 14h2M12 18h2M16 18h2M20 18h2"/></svg>
    <div><h5>Call us</h5><p>(02) 5550 1842</p><em>Customer support troll free</em></div>
  </div>
  <div class="abs contact-item ci-mail">
    <svg viewBox="0 0 28 28" fill="none" stroke="#fff" stroke-width="1.3"><path d="M3 12 14 4l11 8v13H3z"/><path d="M3 12l11 8 11-8"/><rect x="7" y="7" width="14" height="8"/></svg>
    <div><h5>Email us</h5><p>support@pelmorahearing.com</p><em>Normally Respond in 5-6 Hours</em></div>
  </div>
  <div class="abs contact-item ci-news">
    <svg viewBox="0 0 28 28" fill="none" stroke="#fff" stroke-width="1.3"><rect x="2" y="8" width="24" height="14" rx="1"/><path d="M2 22h24v2H2zM8 8l6-5 6 5M9 12h10M9 16h10"/></svg>
    <div><h5>Sign up for our newsletter</h5><div class="news-field"><span>Your E-Mail address</span><span>➤</span></div></div>
  </div>
</section>

<footer class="site-footer">
  <div class="abs foot-head" style="left:82px">Our Locations</div>
  <div class="abs foot-head" style="left:366px">Working Hours</div>
  <div class="abs foot-head" style="left:503px">Navigation</div>
  <div class="abs foot-col" style="left:82px"><h6>Harbourview</h6>Ground Floor, Suite 4,<br>18 Larkin Parade,<br>&nbsp;Harbourview, NSW, 2071<br>Phone: 5550 1842</div>
  <div class="abs foot-col" style="left:216px"><h6>Elm Bay</h6>Shop 2, 47 Corran Street<br>Elm Bay,<br>NSW, 2049<br>Phone : &nbsp;5550 3967</div>
  <div class="abs foot-col" style="left:368px;top:44px">Monday - Friday<br><em style="color:#cfcfcf">08.00 am - 10.00 pm</em><br>Saturday &amp; Sunday<br><em>Closed</em></div>
  <div class="abs foot-col" style="left:503px;top:42px;line-height:11.2px">Home<br>Your Hearing<br>Musicians<br>Doctors Information<br>About us<br>Contact us</div>
  <div class="abs foot-rule"></div>
  <div class="abs copyright">© Pelmora Hearing 2018.com. All rights Reserved Terms and Conditions</div>
  <div class="abs social"><i></i><i></i><i></i><i></i></div>
</footer>

</body>
</html>
```